DOUBLE SIDED BROCHURE NEEDED TO PROMOTE DOCTOR

I need a double sided DL size (99mm x 210mm) brochure, promoting a doctor seeing patients in a new area.

I want something professional. I have included the relevant information. I would also like the Dr's picture somwhere in the brochure, with a professional background. I wish to print these tomorrow, so i will pick a winner within 14 hours of posting this ad.

I have included an example of a brochures design that I recently saw, and its definietly a good starting point.

Medical

```html
<!DOCTYPE html>
<html lang="en">
<head>
<meta charset="utf-8">
<title>Dr. Samir Haddad – DL Brochure</title>
<link href="https://fonts.googleapis.com/css2?family=Oswald:wght@300;400;500&family=Arimo:wght@700&display=swap" rel="stylesheet">
<style>
  :root {
    --stage: #d4d6d9;
    --paper: #ececed;
    --navy: #2e3192;
    --orange: #f7941d;
    --orange-deep: #e8491d;
    --ink: #1d1d1f;
    --white: #ffffff;
    --pink: #d46bb5;
    --purple: #6c6fb5;
    --sky: #7fcbe6;
    --green: #8cc86a;
  }
  * { box-sizing: border-box; margin: 0; padding: 0; }
  html, body { width: 1016px; height: 1200px; overflow: hidden; }
  body { background: var(--stage); font-family: "Oswald", sans-serif; position: relative; }

  .panel {
    position: absolute; top: 110px; width: 462px; height: 980px;
    background: var(--paper); overflow: hidden;
    box-shadow: 0 6px 18px rgba(0,0,0,.25);
  }
  .panel--front { left: 26px; }
  .panel--back { left: 528px; }

  .swoosh { position: absolute; left: 0; width: 100%; }
  .swoosh--top { top: 0; height: 260px; }
  .swoosh--bottom { bottom: 0; height: 140px; }

  .intro-disc {
    position: absolute; left: -60px; top: 165px; width: 610px; height: 610px;
    border-radius: 50%; background: var(--navy);
  }
  .intro {
    position: absolute; left: 40px; top: 262px; width: 390px;
    color: var(--white); text-align: center;
  }
  .intro__greeting { font-size: 31px; font-weight: 500; line-height: 1.2; margin-bottom: 4px; }
  .intro__body { font-size: 19px; font-weight: 400; line-height: 1.3; }
  .contact { margin-top: 18px; color: var(--orange); font-weight: 400; line-height: 1; }
  .contact__label { font-size: 32px; }
  .contact__phone { font-size: 48px; }
  .contact__fax { color: var(--white); font-size: 16px; margin-top: 6px; }

  .portrait {
    position: absolute; left: 226px; top: 640px; width: 200px; height: 200px;
    border-radius: 50%; padding: 10px;
    background: linear-gradient(135deg, var(--orange-deep), var(--orange));
    box-shadow: 0 4px 10px rgba(0,0,0,.3);
  }
  .portrait__photo {
    width: 100%; height: 100%; border-radius: 50%;
    background: linear-gradient(180deg, #a9bfd6 0%, #c8d2dc 45%, #3a3f4c 100%);
  }

  .address-card {
    position: absolute; left: 38px; top: 852px; width: 300px; height: 86px;
    background: var(--white); border-radius: 10px; padding: 10px 16px;
    box-shadow: 0 4px 10px rgba(0,0,0,.22);
    font-family: "Arimo", sans-serif; font-weight: 700; font-size: 18px; color: var(--ink); line-height: 1.2;
  }
  .address-card__line { display: flex; align-items: center; gap: 6px; }
  .address-card__line svg { width: 16px; height: 16px; flex: none; fill: var(--navy); }

  .photo-grid {
    position: absolute; left: 0; top: 0; width: 462px;
    display: grid; grid-template-columns: repeat(3, 1fr); grid-auto-rows: 134px; gap: 2px;
    background: var(--white);
  }
  .photo-grid__tile { display: block; }

  .profile-card {
    position: absolute; left: 40px; top: 330px; width: 398px; height: 560px;
    background: var(--white); border-radius: 26px; padding: 30px 28px;
    box-shadow: 0 6px 16px rgba(0,0,0,.22); color: var(--ink);
  }
  .profile-card__name { font-size: 32px; font-weight: 400; line-height: 1.15; }
  .profile-card__lead { font-size: 20px; font-weight: 400; line-height: 1.3; margin-bottom: 22px; }
  .service-list { list-style: none; font-size: 19px; font-weight: 400; line-height: 1.3; margin-bottom: 22px; }
  .service-list li { position: relative; padding-left: 28px; margin-bottom: 3px; }
  .service-list li::before {
    content: ""; position: absolute; left: 2px; top: 8px; width: 14px; height: 14px; border-radius: 50%;
    background: radial-gradient(circle at 35% 35%, var(--orange), var(--orange-deep));
  }
  .profile-card__sub { font-size: 20px; margin-bottom: 10px; }
</style>
</head>
<body>

<section class="panel panel--front">
  <svg class="swoosh swoosh--top" viewBox="0 0 462 260" preserveAspectRatio="none" aria-hidden="true">
    <path d="M0 120 C120 40 300 30 462 60" fill="none" stroke="var(--pink)" stroke-width="7"/>
    <path d="M0 140 C120 70 300 60 462 80" fill="none" stroke="var(--purple)" stroke-width="6"/>
    <path d="M0 200 C100 120 250 95 420 95" fill="none" stroke="var(--sky)" stroke-width="14"/>
    <path d="M0 225 C90 150 220 125 360 120" fill="none" stroke="var(--green)" stroke-width="14"/>
  </svg>
  <svg class="swoosh swoosh--bottom" viewBox="0 0 462 140" preserveAspectRatio="none" aria-hidden="true">
    <path d="M0 30 C120 60 260 60 462 20" fill="none" stroke="var(--sky)" stroke-width="2"/>
    <path d="M0 130 C140 70 320 70 462 95" fill="none" stroke="var(--purple)" stroke-width="8"/>
    <path d="M0 140 C160 90 330 95 462 115" fill="none" stroke="var(--pink)" stroke-width="8"/>
    <path d="M300 75 C380 60 430 50 462 40" fill="none" stroke="var(--green)" stroke-width="10"/>
  </svg>

  <div class="intro-disc"></div>
  <div class="intro">
    <p class="intro__greeting">Dear Doctors,</p>
    <p class="intro__body">We are pleased to announce that Dr. Samir Haddad is now consulting in Bayview, seeing public and private patients. Guaranteed appointment within two weeks, with patients having the option of surgery at Coastal Health Campus, Harbourside Hospital or St. Clement Private.</p>
    <p class="contact"><span class="contact__label">Contact: </span><span class="contact__phone">1300 555 014</span></p>
    <p class="contact__fax">Please send all referrals by fax to (08) 5550 2841.</p>
  </div>

  <div class="portrait">
    <div class="portrait__photo" role="img" aria-label="Portrait photo of Dr. Samir Haddad against a sky background"></div>
  </div>

  <div class="address-card">
    <p class="address-card__line"><svg viewBox="0 0 16 16"><path d="M8 1 L1 8 H3 V15 H6.5 V10.5 H9.5 V15 H13 V8 H15 Z"/></svg>Bayview Clinic:</p>
    <p class="address-card__line"><svg viewBox="0 0 16 16"><path d="M4.5 0.5 H11.5 A1.5 1.5 0 0 1 13 2 V14 A1.5 1.5 0 0 1 11.5 15.5 H4.5 A1.5 1.5 0 0 1 3 14 V2 A1.5 1.5 0 0 1 4.5 0.5 Z M5 2.5 V12 H11 V2.5 Z"/></svg>42 Kestrel Road</p>
    <p class="address-card__line"><svg viewBox="0 0 16 16"><path d="M1 4 H15 V13 H1 Z M1.5 4.5 L8 9.5 L14.5 4.5" stroke="var(--white)" stroke-width="1"/></svg>Bayview WA 6999.</p>
  </div>
</section>

<section class="panel panel--back">
  <div class="photo-grid">
    <span class="photo-grid__tile" role="img" aria-label="Close-up of a syringe" style="background:linear-gradient(160deg,#c9d3e2,#6f86a8)"></span>
    <span class="photo-grid__tile" role="img" aria-label="Medical worker in mask and goggles" style="background:linear-gradient(180deg,#e6dcd3,#f2f2f2)"></span>
    <span class="photo-grid__tile" role="img" aria-label="Laboratory beaker with green liquid" style="background:linear-gradient(180deg,#e8ecec,#5aa07f)"></span>
    <span class="photo-grid__tile" role="img" aria-label="Doctor taking blood pressure" style="background:linear-gradient(180deg,#f0f0f0,#c9ccd2)"></span>
    <span class="photo-grid__tile" role="img" aria-label="Stethoscope" style="background:linear-gradient(180deg,#fafafa,#e3e3e3)"></span>
    <span class="photo-grid__tile" role="img" aria-label="Nurse preparing an injection" style="background:linear-gradient(180deg,#e2d3c6,#c2aa98)"></span>
    <span class="photo-grid__tile" role="img" aria-label="Medicine bottle" style="background:linear-gradient(180deg,#a06c3f,#4a2f1b)"></span>
    <span class="photo-grid__tile" role="img" aria-label="Sample vial with red cap" style="background:linear-gradient(180deg,#f2f2f2,#e3d6d6)"></span>
    <span class="photo-grid__tile" role="img" aria-label="X-ray image" style="background:linear-gradient(180deg,#7f9cc8,#3d5b8c)"></span>
  </div>

  <svg class="swoosh swoosh--bottom" viewBox="0 0 462 140" preserveAspectRatio="none" aria-hidden="true">
    <path d="M0 30 C150 40 330 30 462 10" fill="none" stroke="var(--sky)" stroke-width="14"/>
    <path d="M200 60 C300 50 400 40 462 30" fill="none" stroke="var(--green)" stroke-width="12"/>
    <path d="M0 75 C160 60 320 80 462 95" fill="none" stroke="var(--purple)" stroke-width="9"/>
    <path d="M0 95 C160 80 320 100 462 115" fill="none" stroke="var(--pink)" stroke-width="8"/>
  </svg>

  <article class="profile-card">
    <h2 class="profile-card__name">Dr. Haddad</h2>
    <p class="profile-card__lead">is a highly trained specialised surgeon, in all areas of Endocrine, Breast and General Surgery. Including;</p>
    <ul class="service-list">
      <li>Thyroid Surgery</li>
      <li>Parathyroid surgery (including minimally invasive parathyroidectomy)</li>
      <li>Breast Cancer Benign breast lesions</li>
    </ul>
    <p class="profile-card__sub">All areas of general surgery, such as;</p>
    <ul class="service-list">
      <li>Gallbladder surgery</li>
      <li>Hernia surgery</li>
      <li>Haemorrhoids</li>
      <li>Carpal Tunnel</li>
      <li>Vasectomy etc etc…</li>
    </ul>
  </article>
</section>

</body>
</html>
```